Need a business card for our overland brand!

We had the logo made and we need a great design for our business card. Use the logo provide or tweak it however you see fit.

Contact Information for Business Card

Name, Title, Telephone, email, website

```html
<!DOCTYPE html>
<html lang="en">
<head>
<meta charset="utf-8">
<title>Summit Trail – Business Card</title>
<link href="https://fonts.googleapis.com/css2?family=Barlow:ital,wght@0,400;0,600;0,700;1,700&display=swap" rel="stylesheet">
<style>
  :root {
    --page: #ffffff;
    --navy: #283a52;
    --ink: #253752;
    --accent: #1f9dbf;
    --mist: #eceeef;
    --mist-dark: #35495f;
    --border: #7a7a7a;
    --label: #7d7d7d;
  }
  * { margin: 0; padding: 0; box-sizing: border-box; }
  html, body {
    width: 1200px; height: 1000px; overflow: hidden;
    background: var(--page);
    font-family: "Barlow", Arial, sans-serif;
  }
  .canvas { position: relative; width: 1200px; height: 1000px; }

  .card {
    position: absolute; left: 281px; width: 639px; height: 366px; overflow: hidden;
  }
  .card--front { top: 101px; background: #fff; border: 1px solid var(--border); }
  .card--back { top: 561px; background: var(--navy); }

  .backdrop {
    position: absolute; left: 0; top: 28px; width: 100%; height: 210px;
  }
  .card--front .backdrop { background: linear-gradient(180deg, rgba(236,238,239,0) 0%, var(--mist) 45%, rgba(236,238,239,0) 100%); }
  .card--back .backdrop { background: linear-gradient(180deg, rgba(53,73,95,0) 0%, var(--mist-dark) 45%, rgba(53,73,95,0) 100%); }

  .brand-name {
    position: absolute; font-weight: 700; text-transform: uppercase;
    line-height: 0.95; letter-spacing: 0.5px;
  }
  .card--front .brand-name {
    left: 100px; top: 212px; font-size: 44px; color: var(--ink);
  }
  .card--back .brand-name {
    left: 0; width: 100%; text-align: center; top: 138px; font-size: 62px; color: #fff;
  }

  .identity { position: absolute; left: 366px; top: 42px; color: var(--accent); }
  .identity__name { font-size: 24px; font-weight: 700; line-height: 1.1; }
  .identity__title { font-size: 17px; font-weight: 700; font-style: italic; margin-top: 2px; }

  .contact { position: absolute; left: 343px; top: 218px; list-style: none; }
  .contact__item {
    display: flex; align-items: center; gap: 7px; height: 30px;
    font-size: 17px; font-weight: 600; color: var(--ink);
  }
  .contact__icon { width: 18px; height: 18px; fill: var(--accent); flex: none; }

  .side-label {
    position: absolute; left: 0; width: 100%; text-align: center;
    font-size: 16px; color: var(--label);
  }
</style>
</head>
<body>
<main class="canvas">
  <section class="card card--front">
    <div class="backdrop" role="img" aria-label="Faint mountain range decoration"></div>
    <div class="brand-name">Summit<br>Trail</div>
    <div class="identity">
      <div class="identity__name">NAME HERE</div>
      <div class="identity__title">Title</div>
    </div>
    <ul class="contact">
      <li class="contact__item">
        <svg class="contact__icon" viewBox="0 0 24 24"><path d="M6.6 10.8a15.1 15.1 0 0 0 6.6 6.6l2.2-2.2a1 1 0 0 1 1-.25 11.4 11.4 0 0 0 3.6.57 1 1 0 0 1 1 1V20a1 1 0 0 1-1 1A17 17 0 0 1 3 4a1 1 0 0 1 1-1h3.5a1 1 0 0 1 1 1c0 1.25.2 2.45.57 3.57a1 1 0 0 1-.25 1z"/></svg>
        123-123-4567
      </li>
      <li class="contact__item">
        <svg class="contact__icon" viewBox="0 0 24 24"><path d="M2 5h20v14H2z M2 5l10 8 10-8" fill="var(--accent)" stroke="#fff" stroke-width="1.5"/></svg>
        name@summittrail.com
      </li>
      <li class="contact__item">
        <svg class="contact__icon" viewBox="0 0 24 24" fill="none" stroke="var(--accent)" stroke-width="2"><circle cx="12" cy="12" r="9.5"/><ellipse cx="12" cy="12" rx="4" ry="9.5"/><path d="M2.5 12h19M4 7h16M4 17h16"/></svg>
        summittrail.com
      </li>
    </ul>
  </section>
  <p class="side-label" style="top:482px">Front Side</p>

  <section class="card card--back">
    <div class="backdrop" role="img" aria-label="Faint mountain range decoration"></div>
    <div class="brand-name">Summit<br>Trail</div>
  </section>
  <p class="side-label" style="top:942px">Back Side</p>
</main>
</body>
</html>
```